Ruler design for Brodmere Liquid waste

We require a very professional design for our marketing product 'Ruler'.
It will be on a white plastic ruler 315mm long and 39mm high.
0 – 30 on the top (in mm).
0 – 12 on the bottom (in inches).
Numbering in black (to be included as an example only) as it is already printed on the plastic stock.
I want logo, phone number, email and website.
Phone number - 08 8317 4925, email info@bwx.com.au, web www.brodmereliquidwaste.com
Large text - Your Local Grease Trap and Liquid Waste Specialists
Please stick to our colours.
Total workable text area –
Length 312mm
Height 24mm
You must supply Print ready pdf files with
all fonts embedded.
Please include crop marks plus 3mm bleed all round.
Marketing

```html
<!DOCTYPE html>
<html lang="en">
<head>
<meta charset="utf-8">
<title>Brodmere Liquid Waste – Ruler</title>
<link href="https://fonts.googleapis.com/css2?family=Anton&family=Roboto:wght@500&display=swap" rel="stylesheet">
<style>
  :root{
    --navy:#211e56;
    --orange:#f27f1f;
    --white:#ffffff;
    --backdrop:#b4b4b4;
  }
  html,body{margin:0;padding:0;overflow:hidden;}
  body{width:1200px;height:1000px;background:var(--backdrop);position:relative;}
  .ruler{
    position:absolute;left:75px;top:460px;width:1050px;height:80px;
    display:flex;background:var(--white);
    box-shadow:0 3px 8px rgba(0,0,0,.35);
  }
  .brand-panel{
    width:181px;background:var(--navy);
    display:flex;align-items:center;justify-content:center;gap:8px;
  }
  .brand-mark{width:22px;height:22px;border-radius:50%;background:var(--orange);flex:none;}
  .brand-name{
    font-family:"Anton",sans-serif;color:var(--white);font-size:15px;
    line-height:1.05;letter-spacing:.5px;text-transform:uppercase;
  }
  .accent-band{width:15px;background:var(--orange);}
  .message{flex:1;display:flex;flex-direction:column;align-items:center;justify-content:center;}
  .headline{
    font-family:"Anton",sans-serif;color:var(--navy);font-size:26px;
    letter-spacing:.6px;margin:0 0 6px;font-weight:400;
  }
  .contacts{display:flex;gap:34px;font-family:"Roboto",sans-serif;font-weight:500;font-size:12px;color:var(--navy);}
  .contact{display:flex;align-items:center;gap:6px;}
  .contact svg{width:11px;height:11px;fill:var(--orange);}
  .end-panel{width:94px;background:var(--navy);display:flex;align-items:center;justify-content:center;}
  .end-mark{width:44px;height:44px;border-radius:50%;background:var(--orange);}
</style>
</head>
<body>
  <div class="ruler">
    <div class="brand-panel">
      <span class="brand-mark"></span>
      <span class="brand-name">Brodmere<br>Liquid Waste</span>
    </div>
    <div class="accent-band"></div>
    <div class="message">
      <h1 class="headline">Our Local Grease Trap and Liquid Waste Specialists</h1>
      <div class="contacts">
        <span class="contact">
          <svg viewBox="0 0 12 12"><path d="M1 4c0-2 2-3 5-3s5 1 5 3v1H8V3.8C7 3.5 5 3.5 4 3.8V5H1z M3 6h6l1 5H2z"/></svg>
          08 8317 4925
        </span>
        <span class="contact">
          <svg viewBox="0 0 12 12"><path d="M3 1h5v3H3z M1 5h10v6H1z"/></svg>
          08 8317 4926
        </span>
        <span class="contact">
          <svg viewBox="0 0 12 12"><path d="M1 3h10v7H1z" /><path d="M1 3l5 4 5-4" fill="none" stroke="#fff" stroke-width="1"/></svg>
          info@bwx.com.au
        </span>
        <span class="contact">
          <svg viewBox="0 0 12 12"><circle cx="6" cy="6" r="5" fill="none" stroke="#f27f1f" stroke-width="1.2"/><path d="M1 6h10M6 1c-2.5 3-2.5 7 0 10M6 1c2.5 3 2.5 7 0 10" fill="none" stroke="#f27f1f" stroke-width="1"/></svg>
          www.brodmereliquidwaste.com
        </span>
      </div>
    </div>
    <div class="end-panel"><span class="end-mark"></span></div>
  </div>
</body>
</html>
```